Beauty Clinic Treatment Menu (Lumen Nails & Beauty)

Needing a treatment menu designed for a beauty clinic in Whitianga, New Zealand. Like the colours grey, pink, white.
Elegant, Modern and feminine

Lumen Nails & Beauty
Karen Pell
Room3, 48 Tainui Street
Whitianga
0273816240
Karen.lumen@mailbox.test
lumenbeauty.co.nz

Target Market(s)

Females

Industry/Entity Type

Beauty Salon

Font styles to use
Serif

Colors

Requirements
Must have
• Chatterly and Snapgrid logo

```html
<!DOCTYPE html>
<html lang="en">
<head>
<meta charset="utf-8">
<title>Lumen Nails &amp; Beauty – Price List</title>
<link href="https://fonts.googleapis.com/css2?family=Montserrat:wght@300;400;500&family=Yellowtail&display=swap" rel="stylesheet">
<style>
  :root{
    --page:#d9d9d9;
    --pink:#ddbcd8;
    --pink-deep:#d49ccb;
    --cream:#f7f5ef;
    --grey:#b9b9b9;
    --ink:#3a3a3a;
    --ink-soft:#8a8a8a;
    --white:#ffffff;
  }
  *{box-sizing:border-box;margin:0;padding:0}
  html,body{width:1200px;height:2863px;overflow:hidden}
  body{background:var(--page);font-family:"Montserrat",sans-serif;color:var(--ink)}
  .spread{position:absolute;left:60px;width:1080px;height:1280px;display:flex;box-shadow:0 10px 30px rgba(0,0,0,.18)}
  .spread--outside{top:100px}
  .spread--inside{top:1480px}
  .panel{position:relative;width:540px;height:1280px;overflow:hidden}
  .panel--pink{background:var(--pink);color:var(--white);text-align:center;padding:70px 50px}
  .panel--cream{background:var(--cream)}
  .script{font-family:"Yellowtail",cursive;font-weight:400}
  .nails-title{font-size:92px;line-height:1;margin-bottom:36px}
  .service{margin-bottom:34px}
  .service h3{font-weight:400;font-size:23px;letter-spacing:1px;text-transform:uppercase;margin-bottom:8px}
  .service p{font-weight:300;font-size:19px;line-height:1.45}
  .contact-block{position:absolute;left:0;right:0;bottom:70px;text-align:center}
  .contact-block .script{font-size:72px;line-height:1;margin-bottom:14px}
  .contact-block .phone{font-weight:500;font-size:28px;letter-spacing:1px}
  .contact-block .web{font-weight:300;font-size:19px;margin-top:4px}
  .brand{display:flex;align-items:center;justify-content:center;gap:14px;margin-top:110px}
  .brand-dot{width:26px;height:26px;border-radius:50%;background:var(--pink-deep)}
  .brand-name{font-size:44px;font-weight:400;color:var(--pink-deep);letter-spacing:3px}
  .cover-title{text-align:center;color:var(--grey);font-size:90px;line-height:.95;margin-top:70px}
  .cover-rule{width:200px;height:2px;background:var(--grey);margin:34px auto}
  .cover-sub{text-align:center;color:var(--pink-deep);font-size:68px;line-height:1}
  .flowers{position:absolute;left:0;right:0;bottom:0;height:520px;
    background:radial-gradient(ellipse at 40% 55%,#eab8d6 0%,#f1cfe2 35%,rgba(247,245,239,0) 70%),
               radial-gradient(ellipse at 85% 35%,#f3d6e6 0%,rgba(247,245,239,0) 55%),
               linear-gradient(180deg,var(--cream) 0%,#e9ede0 100%)}
  .inside-panel{padding:70px 55px 0}
  .bg-bloom{position:absolute;inset:0 0 170px 0;background:radial-gradient(ellipse at 30% 30%,#eceee6 0%,rgba(247,245,239,0) 60%),radial-gradient(ellipse at 75% 75%,#f1ece8 0%,rgba(247,245,239,0) 55%)}
  .section-title{position:relative;color:var(--pink-deep);font-size:70px;line-height:1;text-align:center;margin-bottom:22px}
  .treatment{position:relative;text-align:center;margin-bottom:26px}
  .treatment h4{font-weight:400;font-size:22px;margin-bottom:6px}
  .treatment .time{font-weight:300;font-size:16px;color:var(--ink-soft)}
  .treatment .desc{font-weight:300;font-size:16px;color:var(--ink-soft);line-height:1.4;max-width:360px;margin:0 auto}
  .price-list{position:relative;list-style:none;text-align:center;font-weight:300;font-size:20px;line-height:1.6;margin-bottom:36px}
  .band{position:absolute;left:0;right:0;bottom:0;height:170px;background:var(--pink);color:var(--white);display:flex;flex-direction:column;justify-content:center;align-items:center;gap:6px}
  .band .phone{font-weight:500;font-size:28px;letter-spacing:1px}
  .band .line{font-weight:300;font-size:20px}
</style>
</head>
<body>

<section class="spread spread--outside">
  <div class="panel panel--pink">
    <h2 class="script nails-title">Nails</h2>
    <div class="service"><h3>Manicure</h3><p>Gel Polish | $45<br>Regular Polish | $40</p></div>
    <div class="service"><h3>Pedicure</h3><p>Gel Polish | $45<br>Regular Polish | $40</p></div>
    <div class="service"><h3>Luxury Pedicure</h3><p>Includes: soak, exfoliation, heel<br>rasping and massage<br>Gel Polish | $60<br>Regular Polish | $55</p></div>
    <div class="service"><h3>Gel Removal &amp; Nail Tidy | $25</h3></div>
    <div class="service"><h3>Add On</h3><p>Gel Removal | $5<br>Keravia | $5 per layer<br>Builder in a bottle | $10<br>Nail Art/Glitter | SPOA</p></div>
    <div class="contact-block">
      <div class="script">Contact</div>
      <div class="phone">0273816240</div>
      <div class="web">www.lumenbeauty.co.nz</div>
    </div>
  </div>
  <div class="panel panel--cream">
    <div class="brand"><span class="brand-dot"></span><span class="brand-name">Lumen</span></div>
    <h1 class="script cover-title">Lumen Nails<br>&amp; Beauty</h1>
    <div class="cover-rule"></div>
    <div class="script cover-sub">Price List</div>
    <div class="flowers" role="img" aria-label="Photograph of pink peonies with green leaves"></div>
  </div>
</section>

<section class="spread spread--inside">
  <div class="panel panel--cream inside-panel">
    <div class="bg-bloom" role="img" aria-label="Faint background photograph of pale flowers"></div>
    <h2 class="script section-title">Facials</h2>
    <div class="treatment"><h4>Deep Cleansing Facial | $75</h4><p class="time">45 Minutes</p><p class="desc">Removes build up of dead skin cells, leaves the skin feel soft and hydrated.</p></div>
    <div class="treatment"><h4>Therapeutic Facial | $105</h4><p class="time">60 Minutes</p><p class="desc">Tailored to suit your skins specific needs.</p></div>
    <div class="treatment"><h4>Rejuvenation Facial | $120</h4><p class="time">60 Minutes</p><p class="desc">Active yet gentle treatment that facilitates dermal rejuvenation.</p></div>
    <div class="treatment"><h4>35% Glycolic Facial | $120</h4><p class="time">60 Minutes</p><p class="desc">Hydrating, deep exfoliation treatment improving skin texture and appearance.</p></div>
    <div class="treatment"><h4>Dermaplaning | $120</h4><p class="desc">Creates a smooth and radiant skin surface. Also removes soft facial hairs.</p></div>
    <div class="band"><span class="phone">0273816240</span><span class="line">48 Tainui Street, Whitianga</span></div>
  </div>
  <div class="panel panel--cream inside-panel">
    <div class="bg-bloom" role="img" aria-label="Faint background photograph of pale flowers"></div>
    <h2 class="script section-title">Eyes</h2>
    <ul class="price-list">
      <li>Silka Lash Lift | $115</li><li>Eyebrow Shape | $19</li><li>Eyebrow Tint | $18</li><li>Eyelash Tint | $25</li><li>Eye Trio | $45</li>
    </ul>
    <h2 class="script section-title">Face</h2>
    <ul class="price-list"><li>Lip | $15</li><li>Chin | $15</li></ul>
    <h2 class="script section-title">Body</h2>
    <ul class="price-list">
      <li>Under Arm | $20</li><li>1/2 Leg | $35</li><li>Full Leg | $55</li><li>1/2 Arm | $30</li><li>Full Arm | $40</li><li>Bikini | $28</li><li>Extended Bikini | $38</li><li>Brazilian (1st time) | $65</li><li>Brazilian (4-6 Weeks) | $50</li><li>Patches | $5</li>
    </ul>
    <div class="band"><span class="line">karen.lumen@mailbox.test</span><span class="line">www.lumenbeauty.co.nz</span></div>
  </div>
</section>

</body>
</html>
```